Web Design For Manufacturing And Outsourcing Company

Pick up the pieces from our previous developer and help us complete our website.

5 pages - Home,Machining,Sourcing,About Us, and Contact

Attached you will find screen shots of previous direction but we're open to new ideas.

We can provide all text and images needed.

Thanks!

5+ page

```html
<!DOCTYPE html>
<html lang="en">
<head>
<meta charset="utf-8">
<title>Kestrel Industries</title>
<link href="https://fonts.googleapis.com/css2?family=Roboto:wght@300;400;500;700;900&display=swap" rel="stylesheet">
<style>
:root{
  --orange:#ef4f1d;
  --ink:#2b2b2b;
  --grey-text:#555;
  --soft:#f4f4f4;
  --white:#ffffff;
  --dark:#3a3a3f;
}
*{margin:0;padding:0;box-sizing:border-box}
html,body{width:807px;height:1200px;overflow:hidden;background:var(--white)}
body{position:relative;font-family:'Roboto',sans-serif;color:var(--ink)}

/* hero */
.hero{position:absolute;left:0;top:0;width:807px;height:412px;overflow:hidden}
.hero-bg{position:absolute;left:0;top:0}
.brand{position:absolute;display:flex;align-items:center;gap:8px;font-weight:700;letter-spacing:2px;text-transform:uppercase}
.brand .mark{display:block}
.brand-top{left:104px;top:36px;color:var(--white);font-size:12px}
.brand-top .mark{width:14px;height:14px;background:var(--white)}
.nav{position:absolute;top:43px;left:348px;display:flex;gap:18px;font-size:10.5px;font-weight:500;text-transform:uppercase}
.nav a{text-decoration:none;color:var(--white)}
.nav a.on-light{color:var(--ink)}
.hero-title{position:absolute;left:115px;top:148px;width:300px;color:var(--white);font-size:22px;font-weight:700;line-height:30px;text-transform:uppercase}
.btn{position:absolute;display:flex;align-items:center;justify-content:center;font-weight:700;text-transform:uppercase;text-decoration:none}
.btn-solid{background:var(--orange);color:var(--white)}
.btn-hero{left:116px;top:248px;width:110px;height:32px;font-size:11px}
.arrow{position:absolute;top:194px;width:36px;height:36px;border-radius:50%;background:rgba(70,70,70,.75);display:flex;align-items:center;justify-content:center}
.arrow svg{display:block}
.arrow-left{left:53px;background:rgba(200,200,200,.55)}
.arrow-right{left:692px}
.hero-tag{position:absolute;left:373px;top:368px;width:60px;text-align:center;font-size:9px;font-weight:700;color:var(--dark);letter-spacing:1px;text-transform:uppercase}

/* services */
.services{position:absolute;left:0;top:412px;width:807px;height:353px}
.services .col-right{position:absolute;left:405px;top:0;width:402px;height:353px;background:var(--soft)}
.service h2{position:absolute;font-size:20px;font-weight:700;text-transform:uppercase;color:var(--ink)}
.icon{position:absolute;top:120px;width:66px;height:66px;border-radius:50%;background:var(--white);box-shadow:0 1px 4px rgba(0,0,0,.18);display:flex;align-items:center;justify-content:center}
.icon svg{display:block}
.service p{position:absolute;top:208px;width:247px;font-size:8.6px;line-height:15.6px;color:var(--grey-text);text-align:justify}
.btn-sm{top:275px;width:110px;height:32px;font-size:10px}
.btn-outline{border:1px solid #aaa;color:var(--orange);background:transparent}
.btn .dot{display:inline-block;width:8px;height:8px;border-radius:50%;margin-left:3px;background:currentColor}

/* contact band */
.cta{position:absolute;left:0;top:765px;width:807px;height:325px}
.cta-bg{position:absolute;left:0;top:0}
.cta-tag{position:absolute;left:0;width:807px;top:80px;text-align:center;font-size:11px;font-weight:700;color:var(--white);letter-spacing:2px;text-transform:uppercase}
.cta h3{position:absolute;left:0;width:807px;top:124px;text-align:center;color:var(--white);font-size:21px;font-weight:400;line-height:29px;text-transform:uppercase}
.btn-cta{left:342px;top:195px;width:137px;height:35px;font-size:12px}

/* footer */
.brand-foot{left:94px;top:1127px;color:var(--dark);font-size:10.5px}
.brand-foot .mark{width:12px;height:12px;background:var(--orange)}
.foot-nav{position:absolute;left:270px;top:1123px;display:flex;gap:13px;font-size:10.5px;font-weight:700;text-transform:uppercase}
.foot-nav a{color:var(--ink);text-decoration:none}
.copy{position:absolute;left:270px;top:1143px;font-size:9px;font-weight:500;color:#666}
.social{position:absolute;left:624px;top:1118px;display:flex;gap:4px}
.social span{width:21px;height:21px;border-radius:50%}
</style>
</head>
<body>

<section class="hero">
  <svg class="hero-bg" width="807" height="412" viewBox="0 0 807 412">
    <defs>
      <linearGradient id="greyPhoto" x1="0" y1="0" x2="1" y2="1">
        <stop offset="0" stop-color="#bdbdbd"/>
        <stop offset=".5" stop-color="#dadada"/>
        <stop offset="1" stop-color="#efefef"/>
      </linearGradient>
      <linearGradient id="warmPhoto" x1="0" y1="0" x2="1" y2="1">
        <stop offset="0" stop-color="#a4563a"/>
        <stop offset=".55" stop-color="#7d4a3b"/>
        <stop offset="1" stop-color="#5e3b33"/>
      </linearGradient>
    </defs>
    <rect role="img" aria-label="Lathe machining a steel shaft" width="807" height="412" fill="url(#greyPhoto)"/>
    <path d="M0,0 L540,0 C560,190 450,395 205,412 C120,416 50,400 0,378 Z" fill="var(--orange)"/>
    <path role="img" aria-label="Close view of a lathe chuck and tooling" d="M0,0 L532,0 C548,190 440,388 205,408 C120,412 50,396 0,374 Z" fill="url(#warmPhoto)"/>
  </svg>

  <div class="brand brand-top"><span class="mark"></span>Kestrel Industries</div>
  <nav class="nav">
    <a href="#">Home</a>
    <a href="#">Machining Capabilities</a>
    <a href="#" class="on-light">Sourcing</a>
    <a href="#" class="on-light">Contact Us</a>
  </nav>

  <h1 class="hero-title">A single point of contact for all your procurement needs</h1>
  <a href="#" class="btn btn-solid btn-hero">Read More</a>

  <div class="arrow arrow-left"><svg width="12" height="14" viewBox="0 0 12 14"><path d="M9,1 L3,7 L9,13" fill="none" stroke="#222" stroke-width="2"/></svg></div>
  <div class="arrow arrow-right"><svg width="12" height="14" viewBox="0 0 12 14"><path d="M3,1 L9,7 L3,13" fill="none" stroke="#fff" stroke-width="2"/></svg></div>
  <div class="hero-tag">Kestrel</div>
</section>

<section class="services">
  <div class="col-right"></div>

  <div class="service">
    <h2 style="left:117px;top:71px">Machining</h2>
    <div class="icon" style="left:110px" role="img" aria-label="Blueprint icon">
      <svg width="40" height="36" viewBox="0 0 40 36" fill="none" stroke="#333" stroke-width="1.4">
        <rect x="4" y="6" width="32" height="24" fill="#f26a3c"/>
        <path d="M12,26 L20,9 L28,26 M15,20 H25"/>
        <path d="M4,30 H36" stroke-width="2"/>
      </svg>
    </div>
    <div class="icon" style="left:192px" role="img" aria-label="Robotic arm icon">
      <svg width="40" height="36" viewBox="0 0 40 36" fill="none" stroke="#333" stroke-width="1.4">
        <rect x="6" y="26" width="28" height="4" fill="#f26a3c"/>
        <path d="M12,26 V20 L20,10 L28,14 V18"/>
        <circle cx="20" cy="10" r="2.5" fill="#f26a3c"/>
        <rect x="24" y="20" width="7" height="6" fill="#f26a3c"/>
      </svg>
    </div>
    <div class="icon" style="left:275px" role="img" aria-label="Packaging icon">
      <svg width="40" height="36" viewBox="0 0 40 36" fill="none" stroke="#333" stroke-width="1.4">
        <rect x="8" y="18" width="14" height="12" fill="#f26a3c"/>
        <rect x="22" y="8" width="12" height="12"/>
        <path d="M12,4 V14 M9,11 L12,14 L15,11 M26,18 V11 M30,18 V11" />
      </svg>
    </div>
    <p style="left:110px">whether prototype, quick-turn, short or medium run roduction, our In-house capabilities can help you with any machining needs you may have.</p>
    <a href="#" class="btn btn-solid btn-sm" style="left:110px">Read More<span class="dot"></span></a>
  </div>

  <div class="service">
    <h2 style="left:446px;top:71px">Sourcing</h2>
    <div class="icon" style="left:447px" role="img" aria-label="Planning board icon">
      <svg width="40" height="36" viewBox="0 0 40 36" fill="none" stroke="#333" stroke-width="1.4">
        <rect x="5" y="6" width="30" height="22"/>
        <path d="M10,12 L20,16 L16,23 L29,20" stroke="#ef4f1d" stroke-dasharray="2 2"/>
        <path d="M5,30 H35" stroke-width="2"/>
      </svg>
    </div>
    <div class="icon" style="left:530px" role="img" aria-label="Checklist icon">
      <svg width="40" height="36" viewBox="0 0 40 36" fill="none" stroke="#333" stroke-width="1.4">
        <rect x="10" y="6" width="20" height="26" fill="#f26a3c"/>
        <rect x="16" y="3" width="8" height="5" fill="#fff"/>
        <path d="M14,14 L16,16 L19,12 M21,14 H27 M14,21 L16,23 L19,19 M21,21 H27" stroke="#fff"/>
      </svg>
    </div>
    <div class="icon" style="left:613px" role="img" aria-label="Delivery truck icon">
      <svg width="40" height="36" viewBox="0 0 40 36" fill="none" stroke="#333" stroke-width="1.4">
        <rect x="6" y="9" width="19" height="15" fill="#ef4f1d" stroke="none"/>
        <path d="M25,13 H31 L35,18 V24 H25 Z" fill="#fff"/>
        <circle cx="12" cy="26" r="3" fill="#fff"/>
        <circle cx="30" cy="26" r="3" fill="#fff"/>
      </svg>
    </div>
    <p style="left:447px">We offer a One Stop Shop solution by leveraging existing relationships and supply base knowledge to source hard to locate items, components and assemblies at the lowest cost</p>
    <a href="#" class="btn btn-outline btn-sm" style="left:445px">Read More<span class="dot"></span></a>
  </div>
</section>

<section class="cta">
  <svg class="cta-bg" width="807" height="325" viewBox="0 0 807 325">
    <defs>
      <linearGradient id="darkPhoto" x1="0" y1="0" x2="1" y2="1">
        <stop offset="0" stop-color="#4a4a50"/>
        <stop offset=".5" stop-color="#2f2f35"/>
        <stop offset="1" stop-color="#55555b"/>
      </linearGradient>
    </defs>
    <path d="M0,0 C300,-6 620,10 807,75 L807,300 C600,305 300,300 0,240 Z" fill="var(--orange)"/>
    <path role="img" aria-label="Machined steel part on a lathe" d="M0,5 C300,0 620,16 807,82 L807,292 C600,296 300,290 0,228 Z" fill="url(#darkPhoto)"/>
    <path d="M0,240 C300,300 600,305 807,300 L807,325 L0,325 Z" fill="var(--white)"/>
  </svg>
  <div class="cta-tag">Kestrel</div>
  <h3>Contact us today with your machining<br>or sourcing needs!</h3>
  <a href="#" class="btn btn-solid btn-cta">Get In Touch</a>
</section>

<footer>
  <div class="brand brand-foot"><span class="mark"></span>Kestrel Industries</div>
  <nav class="foot-nav">
    <a href="#">Home</a>
    <a href="#">Machining Capabilities</a>
    <a href="#">Sourcing</a>
    <a href="#">Contact Us</a>
  </nav>
  <div class="copy">© 2019 Company Name &nbsp;All right reserved</div>
  <div class="social">
    <span style="background:#3b5998"></span>
    <span style="background:#3fa1e0"></span>
    <span style="background:#4c6f9c"></span>
    <span style="background:#1c6aa8"></span>
  </div>
</footer>

</body>
</html>
```